We have a cheerleading competition on Sunday the 30 and I want to encourage parent assistance, support and participation!
Updates

1. Please add:
    Cheer Championship (instead of Cheerleading Competition)

2. Banner: Let's support our Cheerleaders!

Under Banner have the Date in big

Before the Location add:  Joins us at:

Thank you all for your designs and taking the time to submit them. I greatly appreciate them and they were all lovely. I could only pick one though! Hope to have you again on my next project.

Regards, Marisa

Industry/Entity Type

It Support

Requirements
Must have
• Flyer should be 1/2 of an A4 page. kid friendly. The cheerleaders are 6-13 yrs old.
The colors Burgundy, Gold (yellow) and White - It should have the team Eagle design on it. Tarpon Ridge Falcons

Simple design. It will contain an address, times and dates.

should have all of the following information:

Date: Sunday - October 30th 2011
Location: Harbor Crest Arena at the Pellham Coast College
3870 Kestrel Lane
Coral gables, FL 33146
Time: Tickets on sale 8:30AM - Doors Open 9:00AM Starts: 10:00AM
Prices: Adults $10.00 Children $5.00 - Cash Only

```html
<!DOCTYPE html>
<html lang="en">
<head>
<meta charset="utf-8">
<title>Cheer Championship – Tarpon Ridge Falcons</title>
<link href="https://fonts.googleapis.com/css2?family=Anton&family=Codystar:wght@400&family=Russo+One&display=swap" rel="stylesheet">
<style>
  :root {
    --pink: #ff1aa8;
    --pink-deep: #e8008f;
    --pink-light: #ff4fc0;
    --yellow: #fff200;
    --white: #ffffff;
    --silhouette: #120010;
    --burgundy: #8c1028;
  }
  * { margin: 0; padding: 0; box-sizing: border-box; }
  html, body { width: 1200px; height: 900px; overflow: hidden; }
  body { background: var(--pink); }

  .flyer {
    position: relative;
    width: 1200px;
    height: 900px;
    overflow: hidden;
    background: radial-gradient(circle at 50% 46%, var(--pink-light) 0%, var(--pink) 45%, var(--pink-deep) 100%);
    font-family: "Anton", sans-serif;
    color: var(--yellow);
  }

  .team-mark {
    position: absolute;
    top: 14px; left: 0; width: 100%;
    display: flex; justify-content: center; align-items: center; gap: 10px;
    font-family: "Anton", sans-serif;
    font-size: 24px; letter-spacing: 2px;
    color: var(--yellow);
    z-index: 2;
  }
  .team-mark .dot { width: 22px; height: 22px; border-radius: 50%; background: var(--burgundy); }

  .title-cheer {
    position: absolute;
    top: 82px; left: 0; width: 100%;
    text-align: center;
    font-family: "Russo One", sans-serif;
    font-size: 76px; letter-spacing: 38px; padding-left: 38px;
    line-height: 1;
    z-index: 2;
  }
  .title-championship {
    position: absolute;
    top: 160px; left: 0; width: 100%;
    text-align: center;
    font-family: "Codystar", sans-serif;
    font-weight: 400;
    font-size: 132px; line-height: 1; letter-spacing: 2px;
    -webkit-text-stroke: 2px var(--yellow);
    z-index: 2;
  }

  .banner {
    position: absolute;
    top: 312px; left: 0;
    width: 100%; height: 150px;
    background: var(--white);
    border-top: 10px solid var(--yellow);
    border-bottom: 10px solid var(--yellow);
    z-index: 1;
  }
  .banner-stars { position: absolute; top: 0; left: 0; width: 1200px; height: 900px; z-index: 2; }

  .cheerleader {
    position: absolute;
    top: 480px;
    width: 120px; height: 420px;
    background: var(--silhouette);
    border-radius: 60px 60px 20px 20px;
    z-index: 0;
  }
  .cheerleader-left { left: 18px; }
  .cheerleader-right { left: 1062px; }

  .banner-text {
    position: absolute;
    top: 352px; left: 0; width: 100%;
    text-align: center;
    font-family: "Anton", sans-serif;
    font-size: 66px; line-height: 1; letter-spacing: 3px;
    color: var(--yellow);
    -webkit-text-stroke: 3px var(--pink);
    paint-order: stroke fill;
    text-shadow: 3px 3px 0 var(--pink), -3px -3px 0 var(--pink), 3px -3px 0 var(--pink), -3px 3px 0 var(--pink);
    z-index: 3;
  }

  .details { position: absolute; left: 0; width: 100%; text-align: center; line-height: 1; z-index: 3; }
  .event-date { top: 532px; font-size: 64px; letter-spacing: 6px; }
  .venue { top: 610px; font-size: 28px; letter-spacing: 3px; }
  .address { top: 648px; font-size: 28px; letter-spacing: 4px; }
  .times { top: 700px; font-size: 28px; letter-spacing: 2.5px; }
  .prices { top: 750px; font-size: 28px; letter-spacing: 4.5px; padding-left: 80px; }
</style>
</head>
<body>
  <main class="flyer">
    <div class="team-mark"><span class="dot"></span><span>TARPON RIDGE FALCONS</span></div>

    <h1 class="title-cheer">CHEER</h1>
    <div class="title-championship">CHAMPIONSHIP</div>

    <div class="banner"></div>
    <svg class="banner-stars" viewBox="0 0 1200 900" aria-hidden="true">
      <g fill="#ff1aa8">
        <polygon points="600,324 604,335 616,335 606,342 610,354 600,347 590,354 594,342 584,335 596,335"/>
        <polygon points="600,421 604,432 616,432 606,439 610,451 600,444 590,451 594,439 584,432 596,432"/>
        <polygon points="28,388 32,399 44,399 34,406 38,418 28,411 18,418 22,406 12,399 24,399"/>
        <polygon points="1155,388 1159,399 1171,399 1161,406 1165,418 1155,411 1145,418 1149,406 1139,399 1151,399"/>
      </g>
    </svg>

    <div class="cheerleader cheerleader-left" role="img" aria-label="Black silhouette of a jumping cheerleader with arms raised"></div>
    <div class="cheerleader cheerleader-right" role="img" aria-label="Black silhouette of a jumping cheerleader with arms raised"></div>

    <h2 class="banner-text">LET’S SUPPORT OUR CHEERLEADERS!</h2>

    <p class="details event-date">SUNDAY - OCTOBER 30TH 2011</p>
    <p class="details venue">HARBOR CREST ARENA AT THE PELLHAM COAST COLLEGE</p>
    <p class="details address">3870 KESTREL LANE CORAL GABLES, FL 33146</p>
    <p class="details times">TICKETS ON SALE 8:30AM - DOORS OPEN 9:00AM &nbsp;- &nbsp;STARTS: 10:00AM</p>
    <p class="details prices">PRICES: ADULTS $10.00 CHILDREN $5.00 - CASH ONLY</p>
  </main>
</body>
</html>
```